Serene Mind-Rest: Quiet Hour Now, Inc.
Create business card, stationery, envelope design
Professional
Marisol T. Okafor, RN, MSN
Founder/Director
712 Harrowgate Lane, Suite PK3
Brooklyn, New York 11347
Marisol@Quiethournow.com
www.Quiethournow.com
Please use the following pantone colors:
purple [266], blue [279] and yellow [123]
Use purple [266] for font on back of card
Enlightening Others Is Empowerment
Sharing Calm Lifts Others ~ Quiet Hour Now
One Quiet Hour ~ A Gift To Yourself
Hello Designers,
I uploaded my current business card so that you can see what I have already.
I just realized after comparing both cards, I did not add my roles on the business card project!
Please add:
Self-Care Specialist
Holistic Nurse Educator
Certified Wellness Coach/Speaker
Thank you,
Marisol

```html
<!DOCTYPE html>
<html lang="en">
<head>
<meta charset="utf-8">
<title>Serene Mind-Rest: Quiet Hour Now, Inc. — Stationery</title>
<link href="https://fonts.googleapis.com/css2?family=Lato:wght@400;700&display=swap" rel="stylesheet">
<style>
  :root{
    --purple:#6a36a8;
    --blue:#418fde;
    --yellow:#ffc72c;
    --paper:#ffffff;
    --ink:#4a4a5a;
    --backdrop:#e9e6e1;
    --mark-tint:#e4e4ea;
  }
  *{margin:0;padding:0;box-sizing:border-box}
  html,body{width:1200px;height:667px;overflow:hidden;background:var(--backdrop);font-family:"Lato",Arial,sans-serif;color:var(--ink)}
  .canvas{position:relative;width:1200px;height:667px}
  .piece{position:absolute;background:var(--paper);overflow:hidden;box-shadow:0 2px 6px rgba(0,0,0,.18)}
  .piece svg.shape{position:absolute;inset:0;width:100%;height:100%}
  .brand{position:absolute;display:flex;flex-direction:column;align-items:flex-start;gap:3px}
  .brand-row{display:flex;align-items:center;gap:6px}
  .brand-dot{width:14px;height:14px;border-radius:50%;background:var(--yellow);flex:none}
  .brand-name{font-weight:700;color:var(--purple);font-size:12px;line-height:1.1}
  .brand-tag{font-size:6px;color:var(--purple);letter-spacing:.3px}
  .soft-mark{position:absolute;border-radius:50%;background:radial-gradient(circle,var(--mark-tint) 0%,rgba(228,228,234,0) 70%)}
  .small{font-size:6.5px;line-height:1.45;color:var(--ink)}

  .envelope-front{left:24px;top:43px;width:432px;height:221px}
  .envelope-front .brand{left:22px;top:22px}
  .envelope-front .return{position:absolute;left:22px;top:70px}

  .envelope-alt{left:24px;top:348px;width:432px;height:130px}
  .envelope-alt .brand{left:18px;top:14px}
  .envelope-alt .return{position:absolute;left:18px;top:58px}
  .envelope-flap{left:24px;top:478px;width:432px;height:110px}

  .letterhead{left:480px;top:43px;width:396px;height:545px}
  .letterhead .brand{left:18px;top:22px}
  .letterhead .sender{position:absolute;right:20px;top:30px;text-align:right}
  .sender-name{font-size:9px;font-weight:700;color:var(--purple)}
  .sender-role{font-size:7px;color:var(--ink);margin-top:2px}
  .letterhead .footer{position:absolute;left:0;right:0;bottom:8px;text-align:center;font-size:5.5px;color:#fff}

  .card-front{left:893px;top:43px;width:283px;height:161px}
  .card-front .panel{position:absolute;left:0;top:0;width:118px;height:100%;background:var(--blue)}
  .card-front .brand{left:10px;top:38px}
  .card-front .brand-name{color:#fff;font-size:10px}
  .card-front .details{position:absolute;left:130px;top:12px;width:145px}
  .card-front .details .sender-name{font-size:8px}
  .card-front .roles{font-size:6px;line-height:1.4;color:var(--ink);margin-top:3px}
  .card-front .contact{margin-top:18px;font-size:6px;line-height:1.45;text-align:right}

  .card-back{left:893px;top:233px;width:283px;height:158px}
  .card-back .message{position:absolute;left:18px;top:50px;font-size:7.5px;line-height:1.45;color:var(--purple)}
  .card-back .site{position:absolute;left:18px;top:116px;font-size:9px;color:var(--purple)}
</style>
</head>
<body>
<main class="canvas">

  <section class="piece envelope-front">
    <svg class="shape" viewBox="0 0 432 221" preserveAspectRatio="none" aria-hidden="true">
      <path d="M0 0 H170 C110 20 60 60 0 120 Z" fill="var(--blue)"/>
      <path d="M0 190 C150 150 300 170 432 130 V221 H0 Z" fill="var(--blue)"/>
      <path d="M0 186 C150 146 300 166 432 126" stroke="var(--yellow)" stroke-width="2" fill="none"/>
    </svg>
    <div class="soft-mark" role="img" aria-label="Faint decorative emblem" style="left:180px;top:40px;width:90px;height:90px"></div>
    <div class="brand">
      <div class="brand-row"><span class="brand-dot"></span><span class="brand-name">Serene Mind-Rest:<br>Quiet Hour Now</span></div>
      <span class="brand-tag">Calm Through Holistic Wellness</span>
    </div>
    <p class="return small">712 Harrowgate Lane, Suite PK3<br>Brooklyn, New York 11347</p>
  </section>

  <section class="piece envelope-alt">
    <svg class="shape" viewBox="0 0 432 130" preserveAspectRatio="none" aria-hidden="true">
      <path d="M0 0 H150 C100 15 50 35 0 70 Z" fill="var(--blue)"/>
      <path d="M0 118 C140 96 290 112 432 84 V130 H0 Z" fill="var(--blue)"/>
      <path d="M0 115 C140 93 290 109 432 81" stroke="var(--yellow)" stroke-width="2" fill="none"/>
    </svg>
    <div class="soft-mark" role="img" aria-label="Faint decorative emblem" style="left:185px;top:20px;width:80px;height:80px"></div>
    <div class="brand">
      <div class="brand-row"><span class="brand-dot"></span><span class="brand-name">Serene Mind-Rest:<br>Quiet Hour Now</span></div>
    </div>
    <p class="return small">712 Harrowgate Lane, Suite PK3<br>Brooklyn, New York 11347</p>
  </section>

  <section class="piece envelope-flap">
    <svg class="shape" viewBox="0 0 432 110" preserveAspectRatio="none" aria-hidden="true">
      <path d="M0 0 H432 V24 C300 40 150 30 0 46 Z" fill="var(--blue)"/>
      <path d="M0 49 C150 33 300 43 432 27" stroke="var(--yellow)" stroke-width="2" fill="none"/>
      <path d="M0 46 L216 100 L432 24" stroke="#e6e6e6" stroke-width="1" fill="none"/>
    </svg>
    <div class="soft-mark" role="img" aria-label="Small emblem on flap" style="left:200px;top:2px;width:32px;height:32px;background:rgba(255,255,255,.35)"></div>
  </section>

  <section class="piece letterhead">
    <svg class="shape" viewBox="0 0 396 545" preserveAspectRatio="none" aria-hidden="true">
      <path d="M0 0 H90 C55 30 25 60 0 100 Z" fill="var(--blue)"/>
      <path d="M0 505 C130 470 270 500 396 460 V545 H0 Z" fill="var(--blue)"/>
      <path d="M0 500 C130 465 270 495 396 455" stroke="var(--yellow)" stroke-width="2" fill="none"/>
    </svg>
    <div class="soft-mark" role="img" aria-label="Faint decorative emblem" style="left:140px;top:80px;width:110px;height:110px"></div>
    <div class="soft-mark" role="img" aria-label="Faint decorative emblem" style="left:140px;top:370px;width:110px;height:110px"></div>
    <div class="brand">
      <div class="brand-row"><span class="brand-dot"></span><span class="brand-name">Serene Mind-Rest:<br>Quiet Hour Now</span></div>
      <span class="brand-tag">Calm Through Holistic Wellness</span>
    </div>
    <div class="sender">
      <p class="sender-name">Marisol T. Okafor, RN, MSN</p>
      <p class="sender-role">Founder/Director</p>
    </div>
    <p class="footer">712 Harrowgate Lane, Suite PK3 &nbsp;|&nbsp; Brooklyn, New York 11347 &nbsp;|&nbsp; (718) 555-0142 &nbsp;|&nbsp; Marisol@Quiethournow.com &nbsp;|&nbsp; www.Quiethournow.com</p>
  </section>

  <section class="piece card-front">
    <div class="panel"></div>
    <div class="brand">
      <div class="brand-row"><span class="brand-dot"></span><span class="brand-name">Serene Mind-Rest:<br>Quiet Hour Now</span></div>
    </div>
    <div class="details">
      <p class="sender-name">Marisol T. Okafor, RN, MSN</p>
      <p class="roles">Founder/Director<br>Self-Care Specialist<br>Holistic Nurse Educator<br>Certified Wellness Coach/Speaker</p>
      <p class="contact">712 Harrowgate Lane, Suite PK3<br>Brooklyn, New York 11347<br>Marisol@Quiethournow.com<br>www.Quiethournow.com</p>
    </div>
  </section>

  <section class="piece card-back">
    <svg class="shape" viewBox="0 0 283 158" preserveAspectRatio="none" aria-hidden="true">
      <path d="M0 0 H283 V14 C190 34 90 22 0 38 Z" fill="var(--blue)"/>
      <path d="M0 41 C90 25 190 37 283 17" stroke="var(--yellow)" stroke-width="1.5" fill="none"/>
    </svg>
    <p class="message">Enlightening Others Is Empowerment<br>Sharing Calm Lifts Others ~ Quiet Hour Now<br>One Quiet Hour ~ A Gift To Yourself</p>
    <p class="site">www.Quiethournow.com</p>
  </section>

</main>
</body>
</html>
```